bargainmentor.net - Podcast Guest Marketing E-Flyer PDF

Dear Designers:I am in need of an attractive and attention-getting layout and design for a three-page marketing flyer (commonly known as a media one sheet) that will be sent via e-mail, as PDF file, to various Podcast hosts to market me as a guest on their podcasts. I want the design of the document to "mirror" the design and branding on my parent bargainmentor.net website. I am providing ALL the edited and proofread copy and content - the designer just needs to create the design for this marketing document. I want an active PDF document and icons should be used for LinkedIn, Phone, E-mail , and website- with hyperlinks that connect accordingly. I need a fast turnaround.
Updates

Dear Designers - instead of using the photo in the project file of me speaking to the audience for the banner image - I thought it would be a better idea to make this marketing piece specific to Podcast Hosts. Therefore, an image such as the one in the link below would be good to use for a banner image. https://www.pixtrove-example.net/gallery?topic=recording+booth+images&ref=qz7&view=grid&id=Kx93LmPwa2RtVbN8YcQdE4&w=1377&h=804#pic=vRmalqobet:

Target Market(s)

This PDF document will be sent to 650 Podcast hosts in North America via a broadcast e-mail.

Font styles to use
Sans Serif

Colors
ec1f27
ffffff
000000
333333
9d9d9d

Requirements
Must have
• A three-page layout that is easy to navigate in PDF form.
• Proper font styles and sizes for key emphasis areas on the document/
• Consistent branding to mirror my bargainmentor.net parent website
• Must be easy for people to read
• Attention-getting design elements and layout
• Professional and sophisticated design
• Icons for contact information
Should not have
• Should not be cluttered and junky-looking.
• Should not use small font sizes that makes it difficult to read.
• If Podcast hosts are interested in having me as a guest - they will read the content as required on three-pages

```html
<!DOCTYPE html>
<html lang="en">
<head>
<meta charset="utf-8">
<title>bargainmentor.net – Podcast Guest One Sheet, Page 2</title>
<link href="https://fonts.googleapis.com/css2?family=Lato:wght@300;400;700&display=swap" rel="stylesheet">
<style>
  :root{
    --red:#ec1f27;
    --white:#ffffff;
    --black:#000000;
    --ink:#333333;
    --grey:#9d9d9d;
    --rule:#d6d6d6;
    --panel:#f1f1f1;
    --dark:#2f2f2f;
  }
  *{margin:0;padding:0;box-sizing:border-box}
  html,body{width:1200px;height:800px;overflow:hidden;background:var(--white)}
  body{font-family:'Lato',sans-serif;color:var(--ink);position:relative}
  .page{position:absolute;left:122px;top:31px;width:958px;height:740px;border:1px solid var(--rule)}
  .brand{position:absolute;left:170px;top:50px;display:flex;align-items:center;gap:4px;font-size:10px;color:var(--ink)}
  .brand-mark{width:10px;height:10px;background:var(--red)}
  .col{position:absolute;top:76px}
  .col-left{left:170px;width:272px}
  .col-mid{left:464px;width:272px}
  .divider{position:absolute;top:78px;width:2px;height:638px;background:#e4e4e4}
  .divider.one{left:452px}
  .divider.two{left:745px}
  h2{color:var(--red);font-weight:400;font-size:21.5px;line-height:24px;letter-spacing:-.2px}
  .col-mid h2{letter-spacing:-.7px}
  p{font-size:13.6px;line-height:18px;text-align:justify;color:#222;hyphens:auto;-webkit-hyphens:auto}
  .col-left h2{margin-bottom:20px}
  .col-mid h2{margin-bottom:24px}
  .dropcap{float:left;font-size:43px;line-height:34px;margin:1px 3px 0 0;color:#222}
  .gap{margin-top:17px}
  .media-line{text-align:left}
  .num{display:inline-block;background:var(--red);color:var(--white);font-size:12px;line-height:13px;padding:0 3px;margin-right:5px}
  .offer{margin-top:13px}
  .media{position:absolute;left:758px;top:79px;width:272px;height:268px;
    background:linear-gradient(160deg,#8a8580 0%,#6f6a66 45%,#5d5955 100%)}
  .media-caption{position:absolute;left:9px;top:25px;width:260px;color:var(--white);font-size:14px;line-height:18px;text-align:left}
  .badge{position:absolute;background:var(--white)}
  .badge.faint{background:rgba(255,255,255,.75)}
  .testimonials{position:absolute;left:758px;top:368px;width:272px;height:271px;border:2px solid #cfcfcf}
  .t-head{position:absolute;left:11px;top:9px;width:248px;height:61px;background:var(--red);color:var(--white);padding:3px 4px;font-size:12px;line-height:18px}
  .t-head strong{font-weight:700}
  .t-body{position:absolute;left:11px;top:80px;width:248px;height:178px;background:var(--panel);padding:6px 4px}
  .quote{font-size:9.3px;line-height:14.4px;color:#333;text-align:left}
  .qmark{font-size:17px;font-weight:700;line-height:8px;vertical-align:-4px}
  .who{margin-top:7px;font-size:9.5px;line-height:14px}
  .who b{font-weight:700;color:#222}
  .who .role{color:var(--grey)}
  .who i{font-size:8px;color:#555}
  .note{position:absolute;left:757px;top:672px;width:271px;height:43px;background:var(--dark);color:#d8d8d8;font-size:10px;font-weight:300;line-height:13px;padding:8px 9px;white-space:nowrap}
  .note b{color:var(--white);font-weight:700}
  .footer{position:absolute;left:170px;top:743px;font-size:9.5px;color:#555}
</style>
</head>
<body>
  <div class="page"></div>

  <div class="brand"><span class="brand-mark"></span><span>bargainmentor.net</span></div>

  <section class="col col-left">
    <h2>How Podcast Listeners Will Benefit</h2>
    <p><span class="dropcap">M</span>ost people are intimidated by the prospect and process of negotiating–and often view negotiating as an uncomfortable haggling and bargaining process that may involve confrontation, anxiety, and stress. If podcast listeners are like most people – then they probably are concerned about being taken advantage of – or that they are missing out on potential opportunities in their personal, social, and business negotiations.</p>
    <p class="gap">To alleviate your listeners’ concerns, Daniel will provide them with easy-to-understand negotiating strategies, tactics, phrases, and tips they can immediately apply–the moment the podcast episode ends. Your listeners will feel more confident when they are equipped with the powerful and beneficial strategies and techniques that will help them save/make money and arrive at better outcomes when negotiating with customers, clients, suppliers, contractors, financial institutions, retailers, co-workers, colleagues, and family members.</p>
    <p class="media-line">Daniel R. Kestrel in the Media</p>
  </section>

  <div class="divider one"></div>

  <section class="col col-mid">
    <h2>Three Ways You Can Profit From Booking Daniel R. Kestrel on Your Podcast</h2>
    <p>Upon mutual agreement, podcast hosts and listeners can have access to the following money-saving and profit-generating opportunities:</p>
    <p class="offer"><span class="num">1.</span>Podcast hosts will be provided with a specific promotional code to share with your listeners that will entitle them to receive a special one-time discount of $19.95US off the purchase of the MP3 download of the Deal Mastery Toolkit Audio Learning Program available on my online store. Complete download and purchase instructions will be provided to podcast hosts to publish in your notes and also communicate to your listeners.</p>
    <p class="offer"><span class="num">2.</span>Podcast hosts will receive a 10% commission payable on the net sales dollar revenue generated from the sale of MP3 downloads of Daniel’s Deal Mastery Toolkit Audio Learning Program.</p>
    <p class="offer"><span class="num">3.</span>Podcast hosts will receive a 10% referral fee for any corporation or association that books Daniel for a presentation, seminar, or learning workshop that directly results from my participation on your podcast.</p>
  </section>

  <div class="divider two"></div>

  <div class="media" role="img" aria-label="Photo of Daniel speaking to a seated audience, overlaid with media outlet badges">
    <p class="media-caption">written articles or contributed to articles for the following media outlets:</p>
    <span class="badge" style="left:12px;top:115px;width:122px;height:22px"></span>
    <span class="badge" style="left:147px;top:115px;width:118px;height:24px"></span>
    <span class="badge" style="left:12px;top:171px;width:118px;height:22px"></span>
    <span class="badge" style="left:145px;top:171px;width:120px;height:22px"></span>
    <span class="badge" style="left:12px;top:215px;width:118px;height:24px"></span>
    <span class="badge faint" style="left:223px;top:215px;width:36px;height:40px"></span>
  </div>

  <section class="testimonials">
    <div class="t-head"><strong>Testimonials:</strong><br>What Some Clients Are Saying About the Bargain Mentor®</div>
    <div class="t-body">
      <p class="quote"><span class="qmark">“</span>Daniel Kestrel did a terrific job on my podcast. His negotiating insights and tips were well received by my listeners, and he was an engaging, knowledgeable, and entertaining guest. Given my expertise in real estate, I thought I was a good negotiator – until Daniel taught me a few new strategies and tips during the podcast. I would recommend Daniel to any podcast host – he is a pro and his topics are relevant and can benefit everyone. <span class="qmark">”</span></p>
      <div class="who"><b>Owen Hartley</b><br><span class="role">Podcast Host</span><br><i>Property Builders Roundtable Podcast, San Antonio, Texas</i></div>
    </div>
  </section>

  <div class="note"><b>Note:</b> Discount and commission payments are subject<br>to agreement to standard terms and conditions</div>

  <div class="footer">2 | Negotiating and Decision Making</div>
</body>
</html>
```